Business card design for a dynamic IT consulting company

We need a business card design for a young firm, specialized in the Telecommunications/Consulting industry. The name of the company is Brask and Partners Business Consulting Ltd. (Short name: Brask and Partnes)
Brask = solve read reverse, so we aim to be uncomplicated and solution-oriented. The small pipe in our logo is also related to the word solve. So we need a new business card design, which is simple, eye catching and something non traditional (I would probably prefer a square shaped design rather than a rectangle, but open for suggestions). Attached our logo.

Target Market(s)

Usually our customers are Tier1 Telecoms providers (Q-Linkra, Parnexo, etc) and their executives.

Industry/Entity Type

Business

Contact Information for Business Card

Name: Gergely Halmindo
Email: g.halmindo@braskpartnera.hu
Web: www.braskpartnera.hu
Mobile: +36 30 555 0192
Title: Managing Director

Optional:
Company name: Brask and Partners Ltd.
Address: 1047 Budapest, Ravaszi str. 17/B, Hungary

Font styles to use
Other font styles liked:
• helveticaneue_medium, Prime Regular are used now.

Colors

Designer to choose colors to be used in the design.

Requirements
Must have
• I would like to have a 2 sided design.
Nice to have
• I thought if we make the logo a bit bigger (without the company name), that could go to the back with the company name below. I though, if the pipe in the logo is somehow touchable on the business card, would be nice and unique.

```html
<!DOCTYPE html>
<html lang="en">
<head>
<meta charset="utf-8">
<title>Brask &amp; Partners – Business Card</title>
<link rel="stylesheet" href="https://fonts.googleapis.com/css2?family=Oswald:wght@700&family=Roboto:wght@400;500&display=swap">
<style>
  :root {
    --backdrop: #5e5e5e;
    --card-dark: #3a3a3c;
    --card-light: #ffffff;
    --ink: #2f2f31;
    --accent-blue: #1a93d6;
    --accent-magenta: #b5348f;
    --white: #ffffff;
  }
  html, body {
    margin: 0;
    padding: 0;
    width: 1200px;
    height: 772px;
    overflow: hidden;
    background: var(--backdrop);
    font-family: "Roboto", Arial, sans-serif;
  }
  .canvas {
    position: relative;
    width: 1200px;
    height: 772px;
  }
  .card {
    position: absolute;
    top: 166px;
    width: 439px;
    height: 440px;
    overflow: hidden;
  }
  .card--front { left: 114px; background: var(--card-light); }
  .card--back  { left: 644px; background: var(--card-dark); }

  .front-header {
    position: absolute;
    left: 0; top: 0;
    width: 100%;
    height: 146px;
    background: var(--card-dark);
  }
  .brand {
    position: absolute;
    display: flex;
    align-items: center;
    gap: 12px;
    color: var(--white);
    font-weight: 400;
    white-space: nowrap;
  }
  .brand__mark {
    width: 14px;
    height: 14px;
    background: var(--accent-magenta);
  }
  .front-header .brand {
    left: 44px;
    top: 48px;
    font-size: 36px;
  }
  .card--back .brand {
    left: 0; right: 0;
    top: 230px;
    justify-content: center;
    font-size: 38px;
  }

  .person {
    position: absolute;
    left: 44px;
    top: 226px;
  }
  .person__name {
    margin: 0;
    font-family: "Oswald", Impact, sans-serif;
    font-weight: 700;
    font-size: 24px;
    line-height: 1;
    letter-spacing: 0.2px;
    color: var(--ink);
    text-transform: uppercase;
    transform: scaleX(0.95);
    transform-origin: left;
  }
  .person__title {
    margin: 6px 0 0;
    font-size: 15px;
    color: var(--accent-blue);
  }

  .contacts {
    position: absolute;
    left: 43px;
    top: 309px;
    margin: 0;
    padding: 0;
    list-style: none;
    font-size: 15px;
    color: var(--ink);
  }
  .contacts li {
    display: flex;
    align-items: center;
    gap: 5px;
    height: 22.5px;
  }
  .contacts strong { font-weight: 500; }
  .contact-icon { width: 17px; height: 17px; flex: none; }

  .address {
    position: absolute;
    left: 44px;
    top: 387px;
    margin: 0;
    font-size: 15.5px;
    color: var(--ink);
  }
</style>
</head>
<body>
<main class="canvas">

  <section class="card card--front" aria-label="Card front">
    <header class="front-header">
      <div class="brand"><span class="brand__mark"></span>Brask &amp; Partners</div>
    </header>

    <div class="person">
      <h1 class="person__name">Gergely Halmindo</h1>
      <p class="person__title">Managing Director</p>
    </div>

    <ul class="contacts">
      <li>
        <svg class="contact-icon" viewBox="0 0 20 20" aria-hidden="true">
          <circle cx="10" cy="10" r="10" fill="var(--accent-magenta)"/>
          <path d="M5 8.5c0-2 2.2-3 5-3s5 1 5 3l-1.6.6-.6-1.4c-1.8-.5-3.8-.5-5.6 0l-.6 1.4z" fill="#fff"/>
          <rect x="6.5" y="10" width="7" height="4" rx="1" fill="#fff"/>
        </svg>
        +36 30 555 0192
      </li>
      <li>
        <svg class="contact-icon" viewBox="0 0 20 20" aria-hidden="true">
          <circle cx="10" cy="10" r="10" fill="var(--accent-magenta)"/>
          <rect x="5" y="6.5" width="10" height="7" fill="none" stroke="#fff" stroke-width="1.2"/>
          <path d="M5 6.5l5 4 5-4M5 13.5l3.6-3.2M15 13.5l-3.6-3.2" fill="none" stroke="#fff" stroke-width="1.1"/>
        </svg>
        g.halmindo@braskpartnera.hu
      </li>
      <li>
        <svg class="contact-icon" viewBox="0 0 20 20" aria-hidden="true">
          <circle cx="10" cy="10" r="10" fill="var(--accent-magenta)"/>
          <g fill="none" stroke="#fff" stroke-width="1">
            <circle cx="10" cy="10" r="5.5"/>
            <ellipse cx="10" cy="10" rx="2.4" ry="5.5"/>
            <path d="M4.5 10h11M5.3 7.3h9.4M5.3 12.7h9.4"/>
          </g>
        </svg>
        <span>www.<strong>braskpartnera</strong>.hu</span>
      </li>
    </ul>

    <p class="address">1047 Budapest, Ravaszi str. 17/B, Hungary</p>
  </section>

  <section class="card card--back" aria-label="Card back">
    <div class="brand"><span class="brand__mark"></span>Brask &amp; Partners</div>
  </section>

</main>
</body>
</html>
```